Movie poster for short film: TINFOIL

We need a creative, artistic, stylized poster design for our short film TINFOIL. We would like to see designs with graphics and bold colors more than photographs. The photographs we are posting are more for reference- you do not have to use them in the poster! We are looking for something clean and simple. The film is a drama so please don't make it funny. The mood of the film is thoughtful and introspective. Name of film should be in all caps. Things to include in the poster:
Name of film: TINFOIL
Velvet Harbor Pictures
Starring Marisa Calloway

Here is a brief plot synopsis: TINFOIL follows one night in the life of a rebellious young woman who breaks into a diner after hours with a can of spray paint. Her intentions change after she ends up discovering what's left of a love story.

The movie is somewhat experimental, set to music for part of it with no dialog. The whole movie takes place in an old fashioned diner.

Target Market(s)

Film festival attendees between the ages of 20-50

Industry/Entity Type

Movie

Font styles to use
Sans Serif

Requirements
Must have
• See project description above- also the film is somewhat dark in nature so please don't make it too 'happy' looking.

```html
<!DOCTYPE html>
<html lang="en">
<head>
<meta charset="utf-8">
<title>TINFOIL – poster set</title>
<link rel="stylesheet" href="https://fonts.googleapis.com/css2?family=Oswald:wght@300;400;500;600&family=Pacifico&display=swap">
<style>
  :root {
    --paper: #ffffff;
    --ink: #f4f1ec;
    --candy-red: #9e2431;
    --candy-rose: #b83a48;
    --candy-teal: #0d6b5c;
    --candy-teal-light: #15826f;
    --candy-lime: #6b8a34;
    --candy-orange: #a85a1e;
    --candy-amber: #b97a2a;
    --shade: rgba(10, 8, 12, 0.55);
    --badge: rgba(244, 241, 236, 0.8);
  }
  * { margin: 0; padding: 0; box-sizing: border-box; }
  html, body { width: 1200px; height: 900px; overflow: hidden; background: var(--paper); }
  .sheet { position: relative; width: 1200px; height: 900px; }

  .poster-slot { position: absolute; }
  .poster-slot--hero { left: 307px; top: 5px; }
  .poster-slot--small { transform-origin: 0 0; transform: scale(0.4846); }
  .slot-tl { left: 16px; top: 5px; }
  .slot-bl { left: 16px; top: 442px; }
  .slot-tr { left: 902px; top: 5px; }
  .slot-br { left: 902px; top: 442px; }

  .poster { position: relative; width: 584px; height: 885px; overflow: hidden; color: var(--ink); }
  .poster-photo {
    position: absolute; inset: 0;
    background:
      radial-gradient(ellipse at 50% 45%, transparent 35%, var(--shade) 100%),
      radial-gradient(circle at 238px 170px, var(--candy-rose) 0, var(--candy-red) 150px, transparent 168px),
      radial-gradient(circle at 290px 520px, var(--candy-teal-light) 0, var(--candy-teal) 160px, transparent 180px),
      radial-gradient(circle at 520px 160px, var(--candy-amber) 0, var(--candy-orange) 120px, transparent 140px),
      radial-gradient(circle at 40px 420px, var(--candy-lime) 0, #55702a 120px, transparent 140px),
      radial-gradient(circle at 290px 900px, var(--candy-amber) 0, var(--candy-orange) 150px, transparent 175px),
      linear-gradient(180deg, #3d3a22 0%, #4a2a1c 50%, #2e1a18 100%);
  }
  .title-word {
    position: absolute; font-family: "Oswald", sans-serif; font-weight: 500;
    text-transform: uppercase; line-height: 1; letter-spacing: 4px;
    color: var(--ink); white-space: nowrap; text-align: center;
    transform: rotate(-6deg);
  }
  .title-word--first { left: 88px; top: 80px; width: 300px; font-size: 150px; }
  .title-word--second { left: 120px; top: 425px; width: 340px; font-size: 150px; }

  .studio-line {
    position: absolute; left: 0; right: 0; top: 748px; padding-left: 20px;
    text-align: center; font-family: "Pacifico", cursive; font-size: 24px; line-height: 1.2;
  }
  .presents {
    position: absolute; left: 0; right: 0; top: 786px; padding-left: 20px;
    text-align: center; font-family: "Oswald", sans-serif; font-weight: 300; font-size: 14px;
  }
  .studio-mark { position: absolute; left: 98px; top: 812px; width: 72px; text-align: center; }
  .studio-mark-square { display: block; width: 14px; height: 22px; background: var(--ink); margin: 0 auto 6px; }
  .studio-mark-name { display: block; font-family: "Oswald", sans-serif; font-weight: 400; font-size: 7px; letter-spacing: 0.5px; text-transform: uppercase; line-height: 1.2; }

  .billing {
    position: absolute; left: 198px; top: 822px; height: 32px;
    font-family: "Oswald", sans-serif; font-weight: 300;
    white-space: nowrap; display: flex; align-items: baseline; gap: 8px;
  }
  .billing-title { font-size: 21px; text-transform: uppercase; }
  .billing-starring { font-size: 11px; }
  .billing-name { font-size: 27px; }

  .web-address { position: absolute; left: 206px; top: 864px; font-family: "Oswald", sans-serif; font-weight: 300; font-size: 9px; }
  .badges { position: absolute; left: 308px; top: 863px; display: flex; gap: 6px; }
  .badge { width: 24px; height: 12px; background: var(--badge); }
  .badge--wide { width: 30px; }
</style>
</head>
<body>
<div class="sheet">

  <div class="poster-slot poster-slot--small slot-tl">
    <div class="poster">
      <div class="poster-photo" role="img" aria-label="Close-up photograph of coloured candy balls in deep, muted tones"></div>
      <div class="title-word title-word--first">Tin</div>
      <div class="title-word title-word--second">Foil</div>
      <p class="studio-line">Velvet Harbor Pictures</p>
      <p class="presents">presents</p>
      <div class="studio-mark"><span class="studio-mark-square"></span><span class="studio-mark-name">Velvet Harbor</span></div>
      <div class="billing"><span class="billing-title">Tinfoil</span><span class="billing-starring">starring</span><span class="billing-name">Marisa Calloway</span></div>
      <p class="web-address">www.velvetharborpictures.com</p>
      <div class="badges"><span class="badge badge--wide"></span><span class="badge"></span><span class="badge"></span><span class="badge"></span></div>
    </div>
  </div>

  <div class="poster-slot poster-slot--small slot-bl">
    <div class="poster">
      <div class="poster-photo" role="img" aria-label="Close-up photograph of coloured candy balls in deep, muted tones"></div>
      <div class="title-word title-word--first">Tin</div>
      <div class="title-word title-word--second">Foil</div>
      <p class="studio-line">Velvet Harbor Pictures</p>
      <p class="presents">presents</p>
      <div class="studio-mark"><span class="studio-mark-square"></span><span class="studio-mark-name">Velvet Harbor</span></div>
      <div class="billing"><span class="billing-title">Tinfoil</span><span class="billing-starring">starring</span><span class="billing-name">Marisa Calloway</span></div>
      <p class="web-address">www.velvetharborpictures.com</p>
      <div class="badges"><span class="badge badge--wide"></span><span class="badge"></span><span class="badge"></span><span class="badge"></span></div>
    </div>
  </div>

  <div class="poster-slot poster-slot--hero">
    <div class="poster">
      <div class="poster-photo" role="img" aria-label="Close-up photograph of coloured candy balls in deep, muted tones"></div>
      <div class="title-word title-word--first">Tin</div>
      <div class="title-word title-word--second">Foil</div>
      <p class="studio-line">Velvet Harbor Pictures</p>
      <p class="presents">presents</p>
      <div class="studio-mark"><span class="studio-mark-square"></span><span class="studio-mark-name">Velvet Harbor</span></div>
      <div class="billing"><span class="billing-title">Tinfoil</span><span class="billing-starring">starring</span><span class="billing-name">Marisa Calloway</span></div>
      <p class="web-address">www.velvetharborpictures.com</p>
      <div class="badges"><span class="badge badge--wide"></span><span class="badge"></span><span class="badge"></span><span class="badge"></span></div>
    </div>
  </div>

  <div class="poster-slot poster-slot--small slot-tr">
    <div class="poster">
      <div class="poster-photo" role="img" aria-label="Close-up photograph of coloured candy balls in deep, muted tones"></div>
      <div class="title-word title-word--first">Tin</div>
      <div class="title-word title-word--second">Foil</div>
      <p class="studio-line">Velvet Harbor Pictures</p>
      <p class="presents">presents</p>
      <div class="studio-mark"><span class="studio-mark-square"></span><span class="studio-mark-name">Velvet Harbor</span></div>
      <div class="billing"><span class="billing-title">Tinfoil</span><span class="billing-starring">starring</span><span class="billing-name">Marisa Calloway</span></div>
      <p class="web-address">www.velvetharborpictures.com</p>
      <div class="badges"><span class="badge badge--wide"></span><span class="badge"></span><span class="badge"></span><span class="badge"></span></div>
    </div>
  </div>

  <div class="poster-slot poster-slot--small slot-br">
    <div class="poster">
      <div class="poster-photo" role="img" aria-label="Close-up photograph of coloured candy balls in deep, muted tones"></div>
      <div class="title-word title-word--first">Tin</div>
      <div class="title-word title-word--second">Foil</div>
      <p class="studio-line">Velvet Harbor Pictures</p>
      <p class="presents">presents</p>
      <div class="studio-mark"><span class="studio-mark-square"></span><span class="studio-mark-name">Velvet Harbor</span></div>
      <div class="billing"><span class="billing-title">Tinfoil</span><span class="billing-starring">starring</span><span class="billing-name">Marisa Calloway</span></div>
      <p class="web-address">www.velvetharborpictures.com</p>
      <div class="badges"><span class="badge badge--wide"></span><span class="badge"></span><span class="badge"></span><span class="badge"></span></div>
    </div>
  </div>

</div>
</body>
</html>
```